Webdesign for a Bikeshop in Innsbruck (submitted designs will be used for Masterthesis anonymously)

To obtain my master's degree, I am conducting a study in the field of web design as part of my master thesis. All submitted designs will therefore be used for study purposes. In order to achieve a homogeneous group, I would like to encourage not only male but also female web designers to submit a design. All submitted designs will be used anonymously for the study and therefore do not allow any conclusions to be drawn about your person. Since this is a contest, the winner will be chosen randomly from all serious submissions. I would be really happy if you would support me in my study. I think the results could be very informative and also useful for your further work (I won't go into more detail here as it could skew the results - but once the contest is over, feel free to contact me. Of course I will also provide you with my results as soon as my work is finished). Below you will find a usecase and a description of what the website should include:

The company Bikeshop Morvalt is planning to relaunch its own website and would like to present itself primarily as a competent and leading consultant in the field of cargo bikes. The design should appeal to a broad audience and embody an urban lifestyle. In any case, the website should include a landing page, a product overview page and a product details page, also make sure to design as gender neutral as possible. You only design the website. So don't worry about hardware or software limitations, just create the best bike store design you can.

1 page

• landing page, product overview page, product details page
• onlineshop

```html
<!DOCTYPE html>
<html lang="en">
<head>
<meta charset="utf-8">
<title>Bikeshop Morvalt</title>
<link href="https://fonts.googleapis.com/css2?family=Playfair+Display:wght@700;800&family=Josefin+Sans:wght@400;600&family=Mulish:wght@400;600;700;800&display=swap" rel="stylesheet">
<style>
:root{
  --accent:#e1461d;
  --ink:#1e1e1e;
  --text:#444;
  --card:#f2f2f4;
  --footer:#1b1b1b;
  --white:#fff;
}
*{margin:0;padding:0;box-sizing:border-box}
html,body{width:1200px;height:4283px;overflow:hidden}
body{position:relative;background:var(--white);font-family:"Mulish",sans-serif;color:var(--text)}
.abs{position:absolute}
.header{left:0;top:0;width:1200px;height:70px;background:var(--white)}
.logo{font-family:"Playfair Display",serif;font-weight:700;font-size:25px;color:var(--ink)}
.header .logo{left:130px;top:17px}
.nav a{position:absolute;top:26px;font-size:14px;color:var(--ink);text-decoration:none}
.nav a.active{color:var(--accent);text-decoration:underline}
.hero{left:0;top:70px;width:1200px;height:588px;
  background:
    radial-gradient(ellipse 420px 260px at 330px 360px,rgba(150,140,130,.55),rgba(150,140,130,0) 70%),
    linear-gradient(180deg,#1f2b14 0%,#2e4020 30%,#4b6330 58%,#7d8a5a 78%,#b9bcb0 92%,#d8d8d2 100%)}
.hero-title{left:670px;top:135px;font-family:"Playfair Display",serif;font-weight:800;font-size:62px;color:var(--white)}
.hero-sub{left:675px;top:225px;width:430px;font-size:21px;line-height:30px;color:var(--white)}
.btn{display:flex;align-items:center;justify-content:center;background:var(--accent);color:var(--white);font-size:13px;text-decoration:none}
.btn-outline{background:var(--white);border:1px solid var(--accent);color:var(--accent)}
.card{background:var(--card);width:576px;height:537px}
.card .photo{position:absolute;left:30px;top:40px;width:516px;height:240px}
.card h3{position:absolute;left:0;width:100%;top:315px;text-align:center;font-family:"Josefin Sans",sans-serif;font-weight:600;font-size:23px;color:var(--accent)}
.card p{position:absolute;left:0;width:100%;top:355px;text-align:center;font-size:15px}
.card .price{top:398px;font-size:17px;font-weight:700;color:var(--ink)}
.card .btn{position:absolute;top:450px;height:35px}
.section-title{width:1200px;left:0;text-align:center;font-family:"Josefin Sans",sans-serif;font-size:24px;color:var(--ink)}
.rule{width:26px;height:2px;background:var(--ink);left:587px}
.feature{width:200px;text-align:center}
.feature svg{display:block;margin:0 auto}
.feature h4{margin-top:30px;font-size:13px;font-weight:800;letter-spacing:.5px;color:var(--ink)}
.feature p{margin-top:12px;font-size:13px;line-height:19px}
.adv-bg{left:0;top:2179px;width:489px;height:479px;background:linear-gradient(160deg,#dfe6c8,#9cb46a 45%,#6a8440 75%,#4f6630)}
.adv-photo{left:489px;top:2179px;width:711px;height:479px;
  background:
    radial-gradient(ellipse 260px 200px at 420px 250px,rgba(45,35,45,.85),rgba(45,35,45,0) 75%),
    linear-gradient(175deg,#a9b98a 0%,#7d9a55 35%,#6b7d52 55%,#9a8f86 78%,#b3aca4 100%)}
.adv-panel{left:131px;top:2179px;width:356px;height:479px;background:var(--white)}
.adv-panel h2{position:absolute;left:47px;top:38px;font-family:"Josefin Sans",sans-serif;font-weight:400;font-size:24px;line-height:29px;color:var(--ink)}
.adv-list{position:absolute;left:49px;top:115px;list-style:none}
.adv-list li{height:28px;font-size:13px;color:var(--ink);display:flex;align-items:center;gap:8px}
.review{width:300px;text-align:center}
.review .q{font-family:"Playfair Display",serif;font-size:54px;font-weight:800;color:var(--ink);line-height:36px;height:30px}
.review .stars{margin-top:4px;color:#f5b400;font-size:15px;letter-spacing:2px}
.review p{margin-top:12px;font-size:16.5px;line-height:24px}
.review .dash{width:22px;height:2px;background:var(--accent);margin:20px auto 0}
.review .name{margin-top:12px;font-size:14px;font-weight:700;color:var(--ink)}
.dots{left:555px;top:3097px;display:flex;gap:8px}
.dots span{width:11px;height:11px;border:1.5px solid #555;border-radius:50%}
.dots span.on{background:var(--accent);border-color:var(--accent)}
.gallery{left:17px;top:3292px;width:1168px;height:531px;display:grid;grid-template-columns:repeat(4,1fr);grid-template-rows:repeat(2,1fr)}
.gallery div{width:100%;height:100%}
.footer{left:0;top:3935px;width:1200px;height:348px;background:var(--footer);color:var(--white)}
.footer h5{position:absolute;font-size:13px;font-weight:800;letter-spacing:.5px}
.fitem{position:absolute;display:flex;align-items:flex-start;gap:12px;font-size:11.5px;line-height:16px}
.ficon{flex:none;width:20px;height:20px;border-radius:50%;background:var(--accent);display:flex;align-items:center;justify-content:center}
.menu-list{position:absolute;left:762px;top:80px;list-style:none;font-size:11.5px;line-height:24px}
.copy{left:0;width:1200px;top:298px;text-align:center;font-size:12px}
</style>
</head>
<body>

<header class="abs header">
  <div class="abs logo">Bikeshop Morvalt</div>
  <nav class="nav">
    <a href="#" class="active" style="left:545px">HOME</a>
    <a href="#" style="left:611px">About us</a>
    <a href="#" style="left:701px">Cargo bikes</a>
    <a href="#" style="left:805px">Accessories</a>
    <a href="#" style="left:913px">Contact us</a>
  </nav>
  <svg class="abs" style="left:1013px;top:27px" width="16" height="16" viewBox="0 0 16 16"><circle cx="6.5" cy="6.5" r="4.8" fill="none" stroke="#111" stroke-width="2"/><path d="M10 10l4.5 4.5" stroke="#111" stroke-width="2.4" stroke-linecap="round"/></svg>
  <svg class="abs" style="left:1048px;top:25px" width="19" height="18" viewBox="0 0 19 18"><path d="M1 2h3l2.5 9h9l2-7H5.5" fill="#111" stroke="#111" stroke-width="1.6" stroke-linejoin="round"/><circle cx="8" cy="15" r="1.7" fill="#111"/><circle cx="14" cy="15" r="1.7" fill="#111"/></svg>
</header>

<section class="abs hero" role="img" aria-label="Person riding a cargo bike along a sunny park path with trees behind"></section>
<svg class="abs" style="left:60px;top:369px" width="24" height="40" viewBox="0 0 24 40"><path d="M20 3L4 20l16 17" fill="none" stroke="#fff" stroke-width="3.5"/></svg>
<svg class="abs" style="left:1103px;top:369px" width="24" height="40" viewBox="0 0 24 40"><path d="M4 3l16 17L4 37" fill="none" stroke="#fff" stroke-width="3.5"/></svg>
<h1 class="abs hero-title">Cargo Bikes</h1>
<p class="abs hero-sub">Lorem Ipsum is simply dummy text of the printing and typesetting industry.</p>
<a class="abs btn" style="left:680px;top:316px;width:128px;height:40px;font-size:16px;font-weight:700">Read More</a>

<article class="abs card" style="left:17px;top:675px">
  <div class="photo" role="img" aria-label="Cargo bike with orange box, side view" style="background:radial-gradient(ellipse 240px 90px at 60% 52%,#d9682e 0%,rgba(217,104,46,.35) 45%,rgba(242,242,244,0) 80%),radial-gradient(ellipse 260px 110px at 45% 60%,rgba(40,48,55,.35),rgba(242,242,244,0) 75%)"></div>
  <h3>Lorm Ipsum</h3><p>It is a long established fact that a read</p><p class="price">$2500.00</p>
  <a class="btn btn-outline" style="left:167px;width:105px">Read More</a><a class="btn" style="left:289px;width:106px">Buy Now</a>
</article>
<article class="abs card" style="left:610px;top:675px">
  <div class="photo" role="img" aria-label="Cargo bike with red box, side view" style="background:radial-gradient(ellipse 200px 80px at 65% 45%,#c8281e 0%,rgba(200,40,30,.35) 45%,rgba(242,242,244,0) 80%),radial-gradient(ellipse 260px 110px at 40% 60%,rgba(50,60,100,.35),rgba(242,242,244,0) 75%)"></div>
  <h3>Lorm Ipsum</h3><p>It is a long established fact that a read</p><p class="price">$2500.00</p>
  <a class="btn btn-outline" style="left:167px;width:105px">Read More</a><a class="btn" style="left:289px;width:106px">Buy Now</a>
</article>
<article class="abs card" style="left:17px;top:1233px">
  <div class="photo" role="img" aria-label="Vintage cargo bike with yellow box, side view" style="background:radial-gradient(ellipse 200px 80px at 60% 42%,#c9ad2e 0%,rgba(201,173,46,.35) 45%,rgba(242,242,244,0) 80%),radial-gradient(ellipse 260px 110px at 40% 60%,rgba(60,70,40,.3),rgba(242,242,244,0) 75%)"></div>
  <h3>Lorm Ipsum</h3><p>It is a long established fact that a read</p><p class="price">$2500.00</p>
  <a class="btn btn-outline" style="left:167px;width:105px">Read More</a><a class="btn" style="left:289px;width:106px">Buy Now</a>
</article>
<article class="abs card" style="left:610px;top:1233px">
  <div class="photo" role="img" aria-label="Green cargo bike with black seat box, side view" style="background:radial-gradient(ellipse 150px 90px at 55% 45%,rgba(40,40,42,.75) 0%,rgba(40,40,42,.25) 50%,rgba(242,242,244,0) 80%),radial-gradient(ellipse 250px 110px at 45% 60%,rgba(80,160,60,.45),rgba(242,242,244,0) 75%)"></div>
  <h3>Lorm Ipsum</h3><p>It is a long established fact that a read</p><p class="price">$2500.00</p>
  <a class="btn btn-outline" style="left:167px;width:105px">Read More</a><a class="btn" style="left:289px;width:106px">Buy Now</a>
</article>

<h2 class="abs section-title" style="top:1820px">Why Choose Us</h2>
<div class="abs rule" style="top:1863px"></div>

<div class="abs feature" style="left:118px;top:1926px">
  <svg width="64" height="64" viewBox="0 0 64 64" fill="none" stroke="#e1461d" stroke-width="2"><rect x="12" y="4" width="34" height="48" rx="2"/><path d="M22 56h30a6 6 0 0 0 0-12H46"/><path d="M29 12l7 3v6c0 4-3 7-7 8-4-1-7-4-7-8v-6z"/><path d="M26 20l2.5 2.5L33 18"/><path d="M19 36h20M19 42h14"/></svg>
  <h4>GUARANTEED</h4><p>All our products are guaranteed for 2 years, but you won't need it!</p>
</div>
<div class="abs feature" style="left:364px;top:1926px">
  <svg width="64" height="64" viewBox="0 0 64 64" fill="none" stroke="#e1461d" stroke-width="2"><rect x="8" y="30" width="10" height="24"/><path d="M18 32l10-12 2-10c5 0 6 5 5 11h14c3 0 4 3 3 5 2 1 2 4 0 5 2 1 2 4 0 5 1 2 0 5-3 5H24l-6-3"/><path d="M32 2v4M20 6l2 3M44 6l-2 3M50 14l-4 1"/></svg>
  <h4>QUALITY</h4><p>There are many variations of passages of Lorem Ipsum available but the.</p>
</div>
<div class="abs feature" style="left:613px;top:1926px">
  <svg width="64" height="64" viewBox="0 0 64 64" fill="none" stroke="#e1461d" stroke-width="2"><path d="M14 34V28a18 18 0 0 1 36 0v6"/><rect x="10" y="30" width="9" height="16" rx="3"/><rect x="45" y="30" width="9" height="16" rx="3"/><path d="M50 46c0 8-8 10-16 10"/><rect x="28" y="53" width="7" height="6" rx="2"/></svg>
  <h4>SUPPORT</h4><p>There are many variations of passages of Lorem Ipsum available but the.</p>
</div>
<div class="abs feature" style="left:876px;top:1926px">
  <svg width="64" height="64" viewBox="0 0 64 64" fill="none" stroke="#e1461d" stroke-width="2"><circle cx="12" cy="42" r="9"/><circle cx="52" cy="42" r="9"/><path d="M12 42l8-14h10l6 14h16"/><path d="M36 28h22l-4 14"/><path d="M18 22h6M20 22l2 6"/></svg>
  <h4>14-DAY FREE TRIAL</h4><p>There are many variations of passages of Lorem Ipsum available but the.</p>
</div>

<div class="abs adv-bg" role="img" aria-label="Blurred spring blossoms and greenery"></div>
<div class="abs adv-photo" role="img" aria-label="Child riding in the covered box of a cargo bike on a park path"></div>
<section class="abs adv-panel">
  <h2>The advantages of<br>cargo bikes</h2>
  <ul class="adv-list">
    <li><svg width="9" height="10" viewBox="0 0 9 10"><path d="M1 5h6M4 1.5L7.5 5 4 8.5" fill="none" stroke="#e1461d" stroke-width="2"/></svg>Lorem Ipsum is simply dumm</li>
    <li><svg width="9" height="10" viewBox="0 0 9 10"><path d="M1 5h6M4 1.5L7.5 5 4 8.5" fill="none" stroke="#e1461d" stroke-width="2"/></svg>There are many variations of passa</li>
    <li><svg width="9" height="10" viewBox="0 0 9 10"><path d="M1 5h6M4 1.5L7.5 5 4 8.5" fill="none" stroke="#e1461d" stroke-width="2"/></svg>It is a long established fact that</li>
    <li><svg width="9" height="10" viewBox="0 0 9 10"><path d="M1 5h6M4 1.5L7.5 5 4 8.5" fill="none" stroke="#e1461d" stroke-width="2"/></svg>Lorem ipsum dolor sit amet, consectet</li>
    <li><svg width="9" height="10" viewBox="0 0 9 10"><path d="M1 5h6M4 1.5L7.5 5 4 8.5" fill="none" stroke="#e1461d" stroke-width="2"/></svg>At vero eos et accusamus et iusto</li>
    <li><svg width="9" height="10" viewBox="0 0 9 10"><path d="M1 5h6M4 1.5L7.5 5 4 8.5" fill="none" stroke="#e1461d" stroke-width="2"/></svg>Lorem Ipsum is simply dumm</li>
    <li><svg width="9" height="10" viewBox="0 0 9 10"><path d="M1 5h6M4 1.5L7.5 5 4 8.5" fill="none" stroke="#e1461d" stroke-width="2"/></svg>There are many variations of passa</li>
    <li><svg width="9" height="10" viewBox="0 0 9 10"><path d="M1 5h6M4 1.5L7.5 5 4 8.5" fill="none" stroke="#e1461d" stroke-width="2"/></svg>It is a long established fact that</li>
    <li><svg width="9" height="10" viewBox="0 0 9 10"><path d="M1 5h6M4 1.5L7.5 5 4 8.5" fill="none" stroke="#e1461d" stroke-width="2"/></svg>Lorem ipsum dolor sit amet, consectet</li>
    <li><svg width="9" height="10" viewBox="0 0 9 10"><path d="M1 5h6M4 1.5L7.5 5 4 8.5" fill="none" stroke="#e1461d" stroke-width="2"/></svg>At vero eos et accusamus et iusto</li>
  </ul>
  <a class="abs btn" style="left:49px;top:410px;width:94px;height:35px">Read More</a>
</section>

<h2 class="abs section-title" style="top:2697px">Reviews</h2>
<div class="abs rule" style="top:2740px"></div>
<div class="abs review" style="left:124px;top:2800px"><div class="q">&ldquo;</div><div class="stars">★★★★★</div><p>Sed ut perspiciatis unde omnis iste natus error sit voluptatem accusantium doloremque laudantium, totam rem aperiam, eaque ipsa quae ab illo inventore veritatis et quasi</p><div class="dash"></div><div class="name">Marlen</div></div>
<div class="abs review" style="left:448px;top:2800px"><div class="q">&ldquo;</div><div class="stars">★★★★★</div><p>Sed ut perspiciatis unde omnis iste natus error sit voluptatem accusantium doloremque laudantium, totam rem aperiam, eaque ipsa quae ab illo inventore veritatis et quasi</p><div class="dash"></div><div class="name">Marlen</div></div>
<div class="abs review" style="left:774px;top:2800px"><div class="q">&ldquo;</div><div class="stars">★★★★★</div><p>Sed ut perspiciatis unde omnis iste natus error sit voluptatem accusantium doloremque laudantium, totam rem aperiam, eaque ipsa quae ab illo inventore veritatis et quasi</p><div class="dash"></div><div class="name">Marlen</div></div>
<div class="abs dots"><span></span><span></span><span class="on"></span><span></span><span></span></div>

<h2 class="abs section-title" style="top:3207px">Gallery</h2>
<div class="abs rule" style="top:3250px"></div>
<div class="abs gallery">
  <div role="img" aria-label="Cargo bike rider on a city street" style="background:radial-gradient(ellipse 70px 30px at 55% 75%,rgba(30,30,30,.7),rgba(30,30,30,0)),linear-gradient(180deg,#d8cfc2 0%,#a79d90 50%,#6f6c68 100%)"></div>
  <div role="img" aria-label="Parent with two children in a cargo bike box" style="background:radial-gradient(ellipse 80px 50px at 55% 70%,rgba(214,120,40,.85),rgba(214,120,40,0)),linear-gradient(160deg,#8c7a63,#b89a7a 50%,#3d3a36)"></div>
  <div role="img" aria-label="Cargo bike with grey box parked by a hedge" style="background:radial-gradient(ellipse 70px 45px at 50% 45%,rgba(200,200,205,.9),rgba(200,200,205,0)),linear-gradient(180deg,#4f6e34,#88935f 50%,#9a9a94)"></div>
  <div role="img" aria-label="Cargo bike with orange box on a sidewalk" style="background:radial-gradient(ellipse 80px 55px at 45% 50%,rgba(190,72,32,.95),rgba(190,72,32,0)),linear-gradient(170deg,#9aa39a,#8c867d 55%,#7a756e)"></div>
  <div role="img" aria-label="Courier riding a yellow cargo bike with parcels" style="background:radial-gradient(ellipse 90px 35px at 45% 75%,rgba(225,210,40,.85),rgba(225,210,40,0)),linear-gradient(180deg,#5d6a4a,#8d8c6f 55%,#6d6d6a)"></div>
  <div role="img" aria-label="Father riding a cargo bike with children on a city street" style="background:radial-gradient(ellipse 70px 45px at 50% 70%,rgba(190,110,50,.9),rgba(190,110,50,0)),linear-gradient(170deg,#d4d0c3,#a29a88 60%,#5a5650)"></div>
  <div role="img" aria-label="Black cargo bike in a yellow rapeseed field" style="background:linear-gradient(180deg,#8ea7c4 0%,#c4b04a 40%,#8c8a3a 60%,#3f4b2e 100%)"></div>
  <div role="img" aria-label="Father with child in a black cargo bike by apartment buildings" style="background:radial-gradient(ellipse 80px 50px at 60% 70%,rgba(25,25,28,.85),rgba(25,25,28,0)),linear-gradient(170deg,#d0d6dc,#8d9298 60%,#4b4b4e)"></div>
</div>
<a class="abs btn" style="left:537px;top:3856px;width:126px;height:36px">View All Images</a>

<footer class="abs footer">
  <div class="abs logo" style="left:138px;top:120px;color:#fff;font-size:24px">Bikeshop Morvalt</div>
  <h5 style="left:444px;top:40px">CONTACT US</h5>
  <div class="fitem" style="left:446px;top:81px"><span class="ficon"><svg width="10" height="12" viewBox="0 0 10 12"><path d="M5 11.5S1 7 1 4.5a4 4 0 0 1 8 0C9 7 5 11.5 5 11.5z" fill="#fff"/><circle cx="5" cy="4.5" r="1.4" fill="#e1461d"/></svg></span><span>18 Talweg Lane,<br>Unit 4, Morvalt 6020</span></div>
  <div class="fitem" style="left:446px;top:132px"><span class="ficon"><svg width="10" height="10" viewBox="0 0 10 10"><path d="M2 1l2 2-1 1.5c.6 1.2 1.3 1.9 2.5 2.5L7 6l2 2-1.3 1.3C4.5 9 1 5.5.7 2.3z" fill="#fff"/></svg></span><span>Call Us<br>+43 555 010 2040</span></div>
  <div class="fitem" style="left:446px;top:184px"><span class="ficon"><svg width="11" height="8" viewBox="0 0 11 8"><rect width="11" height="8" rx="1" fill="#fff"/><path d="M.5.8l5 3.6 5-3.6" fill="none" stroke="#e1461d" stroke-width="1"/></svg></span><span>E mail Us<br>info@bikeshopmorvalt.com</span></div>
  <h5 style="left:762px;top:40px">MENU</h5>
  <ul class="menu-list"><li>HOME</li><li>ABOUT US</li><li>CARGO BIKES</li><li>ACCESSORIES</li><li>CONTACT US</li></ul>
  <h5 style="left:969px;top:40px">FOLLOW US</h5>
  <div class="fitem" style="left:967px;top:94px;align-items:center"><span class="ficon" style="width:24px;height:24px"></span><span>Like us on<br>PAGEBOOK</span></div>
  <div class="fitem" style="left:967px;top:144px;align-items:center"><span class="ficon" style="width:24px;height:24px"></span><span>Follow us on<br>CHIRPER</span></div>
  <div class="fitem" style="left:967px;top:195px;align-items:center"><span class="ficon" style="width:24px;height:24px"></span><span>Follow us on<br>WORKNET</span></div>
  <div class="abs copy">Copyright © 2022 All Rights Reserved</div>
</footer>

</body>
</html>
```